VERIX WORDPRESS DESIGN

Hello Happy People,

My name is Jai i run a company called peakmarkhub.net.au am working on a new project with LED lighting and have decided to try craft tribe as i've heard great things.

Our company is in need of wordpress design for a new company 'Verix' we wholesale the best LED lighting products in the world :)

We are targeting commercial customers, small and medium also!

I would like a wordpress design based on the logos, pictures and content that i provide.

We would like to see the design include;
home page
about us Page
Distributors Page
Lighting School Page
small medium enterprise
commercial enterprise
industrial and mining
Categories Page
Contact Us Page

5 year warranty badge included
10 year extended warranty badge included
I have put a catalogue together for the lighting products that looks better then the rubbish on the website.

We will be on linkedin & facebook

Our company website is www.verix.com.au

I am available for the next 10 days to go through with anyone that is interested in taking this project on and will offer work

Industry/Entity Type

School

Requirements
Must have
• banners with factories and commercial lighting products depending on the page

```html
<!DOCTYPE html>
<html lang="en">
<head>
<meta charset="utf-8">
<title>Verix – LED Lighting Wholesale</title>
<link href="https://fonts.googleapis.com/css2?family=Questrial&family=Play:wght@400;700&family=Arimo:wght@700&display=swap" rel="stylesheet">
<style>
:root{
  --green:#4b8e3b;
  --green-dark:#3f7a31;
  --green-deep:#2f6b27;
  --green-band-top:#5aa046;
  --green-band-bottom:#3b7a2f;
  --tab-1:#5ea54a;
  --tab-2:#67b352;
  --tab-3:#72c05c;
  --panel:#efefef;
  --text:#3a3a3a;
  --text-soft:#5a5a5a;
  --white:#ffffff;
  --headline:#3d7a2f;
}
*{margin:0;padding:0;box-sizing:border-box}
html,body{width:1200px;height:965px;overflow:hidden}
body{position:relative;background:linear-gradient(135deg,#d2d4d2 0%,#bfc1bf 40%,#cfd1cf 70%,#b9bbb9 100%);font-family:"Questrial",sans-serif;color:var(--text)}
.header{position:absolute;left:0;top:0;width:1200px;height:208px;background:var(--green);overflow:hidden}
.header-shapes{position:absolute;left:0;top:0}
.nav-band{position:absolute;left:0;top:168px;width:1200px;height:40px;background:linear-gradient(var(--green-band-top),var(--green-band-bottom));box-shadow:0 3px 6px rgba(0,0,0,.35)}
.logo-disc{position:absolute;left:0;top:0;width:330px;height:210px}
.brand{position:absolute;left:144px;top:56px;font-size:40px;line-height:44px;color:#1f1f1f;letter-spacing:.5px}
.brand-url{position:absolute;left:145px;top:95px;font-size:14px;color:#1f1f1f;letter-spacing:.9px}
.main-nav a{position:absolute;top:175px;height:26px;line-height:26px;font-size:18px;color:var(--white);text-decoration:none;white-space:nowrap;letter-spacing:.2px}
.main-nav a.active{left:309px;width:82px;text-align:center;background:var(--white);color:var(--green)}
.social{position:absolute;top:116px;width:41px;height:41px;border-radius:50%;background:radial-gradient(circle at 40% 35%,#6fa864,#2d5c27 70%);border:2px solid #dfe5de;box-shadow:0 2px 4px rgba(0,0,0,.4)}
.panel{position:absolute;left:139px;top:208px;width:922px;height:692px;background:var(--panel);opacity:.93}
.banner{position:absolute;left:174px;top:239px;width:852px;height:242px;background:var(--white);box-shadow:0 2px 4px rgba(0,0,0,.2)}
.tab{position:absolute;top:0;width:29px;height:242px;font-family:"Play",sans-serif;font-size:18px;color:#3b4b36}
.tab span{position:absolute;bottom:8px;left:4px;writing-mode:vertical-rl;transform:rotate(180deg);white-space:nowrap;letter-spacing:.8px;word-spacing:3px}
.banner-photo{position:absolute;left:100px;top:15px;width:345px;height:210px;border-radius:6px;background:radial-gradient(ellipse at 35% 50%,#d8d8d8,#8a8a8a 55%,#fff 80%)}
.banner-title{position:absolute;left:478px;top:46px;font-family:"Play",sans-serif;font-weight:700;font-size:35px;color:var(--headline)}
.banner-sub{position:absolute;left:478px;top:96px;width:280px;text-align:center;font-family:"Play",sans-serif;font-size:24px;line-height:30px;color:#444}
.dot{position:absolute;top:227px;width:8px;height:8px;border-radius:50%}
.side-title{position:absolute;left:173px;top:535px;font-size:17px;color:#111;font-weight:bold}
.category-list{position:absolute;left:178px;top:574px;list-style:none;font-size:13px;line-height:20.8px;color:var(--text-soft);letter-spacing:.4px}
.divider{position:absolute;left:393px;top:535px;width:1px;height:347px;background:#555}
.featured-title{position:absolute;left:437px;top:527px;font-family:"Play",sans-serif;font-weight:700;font-size:26px;color:var(--headline)}
.featured-strip{position:absolute;left:439px;top:557px;width:601px;height:165px;background:var(--white)}
.product{position:absolute;top:4px;width:138px}
.product-frame{width:138px;height:136px;border:1px solid #ddd;display:flex;align-items:center;justify-content:center}
.product-image{width:80px;height:70px;border-radius:50%;background:radial-gradient(circle,#e8e8e8,#9a9a9a 70%)}
.product-code{font-family:"Arimo",sans-serif;font-weight:700;font-size:9px;color:var(--green-deep);margin-top:3px;margin-left:2px}
.photo{position:absolute;top:750px;height:123px}
.footer{position:absolute;left:0;top:900px;width:1200px;height:65px;background:linear-gradient(var(--green-band-top),var(--green-band-bottom))}
.footer-brand{position:absolute;left:145px;top:910px;font-size:17px;color:var(--white)}
.footer-meta{position:absolute;left:145px;top:929px;font-size:13px;line-height:15px;color:var(--white);letter-spacing:.4px}
.footer-social{position:absolute;top:922px;width:25px;height:25px;border-radius:50%;background:radial-gradient(circle at 40% 35%,#6fa864,#2d5c27 70%);border:2px solid #dfe5de}
.footer-nav a{position:absolute;top:926px;font-size:13.5px;color:var(--white);text-decoration:none;white-space:nowrap;letter-spacing:.3px}
</style>
</head>
<body>
<header class="header">
  <svg class="header-shapes" width="1200" height="208">
    <circle cx="460" cy="120" r="180" fill="var(--green-dark)"/>
    <circle cx="460" cy="-40" r="115" fill="var(--green-deep)"/>
  </svg>
</header>
<div class="nav-band"></div>
<svg class="logo-disc" width="330" height="210">
  <path d="M285 0 A160 160 0 0 1 262 208 L276 208 A170 170 0 0 0 300 0 Z" fill="#e6e6e6"/>
  <circle cx="191" cy="77" r="113" fill="var(--white)"/>
</svg>
<div class="brand">Verix</div>
<div class="brand-url">www.verix.com.au</div>
<nav class="main-nav">
  <a class="active">home</a>
  <a style="left:409px">about us</a>
  <a style="left:518px">Distributors</a>
  <a style="left:644px">Lighting School</a>
  <a style="left:813px">Categories</a>
  <a style="left:946px">Contact Us</a>
</nav>
<span class="social" style="left:1075px" aria-label="Social profile link"></span>
<span class="social" style="left:1127px" aria-label="Professional network profile link"></span>

<div class="panel"></div>

<section class="banner">
  <div class="tab" style="left:0;background:var(--tab-1)"><span>higt bay light-</span></div>
  <div class="tab" style="left:29px;background:var(--tab-2)"><span>low bay lighting</span></div>
  <div class="tab" style="left:58px;background:var(--tab-3)"><span>panel lighting</span></div>
  <div class="banner-photo" role="img" aria-label="LED down light fittings, front and side view"></div>
  <div class="banner-title">LED Down Lights</div>
  <div class="banner-sub">See our range<br>Click Here</div>
  <span class="dot" style="left:722px;background:#333"></span>
  <span class="dot" style="left:743px;border:2px solid #333"></span>
  <div class="tab" style="left:765px;background:var(--tab-3)"><span>track lighting</span></div>
  <div class="tab" style="left:794px;background:var(--tab-2)"><span>tubular lighting</span></div>
  <div class="tab" style="left:823px;background:var(--tab-1)"><span>work lighting</span></div>
</section>

<h2 class="side-title">Categories</h2>
<ul class="category-list">
  <li>MR16</li><li>Ceiling Lights</li><li>Down Lights</li><li>EXIT &amp; Emergency Lighting</li><li>LED Globes</li><li>Candle</li><li>Candle Fancy</li><li>High Bay Lighting</li><li>Low Bay Lighting</li><li>Panel Lighting</li><li>PAR Lighting</li><li>Sensor Light</li><li>Track Lighting</li><li>Tubular Lighting</li><li>Work Lighting</li>
</ul>
<div class="divider"></div>

<h2 class="featured-title">Featured</h2>
<section class="featured-strip">
  <div class="product" style="left:5px"><div class="product-frame"><div class="product-image" role="img" aria-label="Small LED down light" style="width:50px;height:45px"></div></div><div class="product-code">VRX5-DL-4K</div></div>
  <div class="product" style="left:155px"><div class="product-frame"><div class="product-image" role="img" aria-label="LED ceiling light"></div></div><div class="product-code">VRX8-CL-85-5K</div></div>
  <div class="product" style="left:305px"><div class="product-frame"><div class="product-image" role="img" aria-label="Large LED ceiling light" style="width:90px;height:85px"></div></div><div class="product-code">VRX25-CL-185-5K</div></div>
  <div class="product" style="left:454px"><div class="product-frame"><div class="product-image" role="img" aria-label="Portable LED work light on yellow stand" style="border-radius:8px;background:linear-gradient(#f2c400,#d9a800 60%,#222)"></div></div><div class="product-code">VRX10-WL-5K</div></div>
</section>

<div class="photo" role="img" aria-label="Commercial office towers against a blue sky" style="left:439px;width:184px;background:linear-gradient(160deg,#9cc3e6,#6b7f92 60%,#3d4a55)"></div>
<div class="photo" role="img" aria-label="Factory warehouse interior with overhead lighting" style="left:644px;width:186px;background:linear-gradient(#cfd6dc,#8e969c 55%,#6a5a4c)"></div>
<div class="photo" role="img" aria-label="Manufacturing floor with machines and green floor" style="left:852px;width:187px;background:linear-gradient(#d9dde0,#9aa3a8 55%,#3fa07a)"></div>

<footer class="footer"></footer>
<div class="footer-brand">Verix</div>
<div class="footer-meta">www.verix.com.au<br>© 2012 Verix</div>
<span class="footer-social" style="left:366px" aria-label="Social profile link"></span>
<span class="footer-social" style="left:404px" aria-label="Professional network profile link"></span>
<nav class="footer-nav">
  <a style="left:523px">home</a>
  <a style="left:587px">about us</a>
  <a style="left:669px">Distributors</a>
  <a style="left:763px">Lighting School</a>
  <a style="left:889px">Categories</a>
  <a style="left:990px">Contact Us</a>
</nav>
</body>
</html>
```